Business Card for Auto Dealership - Clean, sharp and professional

Please use the maroon logo with the grey background. Need a sharp, clean and professional business card for an Auto Dealer. In the files provides there is three different logos. I have not decided which one to go with yet. Right now I am favoring the grey/silver background. I would like my contact info on there and the website as well. I feel like less is more and want something simple, clean and sharp. Thank you in advance for your tie and effort! I also need email signature, letterhead, etc after this

Target Market(s)

Car buyers

Industry/Entity Type

Automotive

Contact Information for Business Card

Dean
555-417-2386
www.BrinwoodAutoHub.example
Dean@BrinwoodAutoHub.example

Font styles to use
Serif
Sans Serif

Requirements
Must have
• Please use the maroon logo with the grey background. Business Card Details and logo from files. Please stick to the logo colors

```html
<!DOCTYPE html>
<html lang="en">
<head>
<meta charset="utf-8">
<title>Brinwood Auto Hub – Business Card</title>
<link rel="stylesheet" href="https://fonts.googleapis.com/css2?family=Saira:wght@700&family=PT+Sans:wght@400&display=swap">
<style>
  :root {
    --backdrop: #4b4b4b;
    --card: #c1c1c1;
    --maroon: #45201f;
  }
  * { margin: 0; padding: 0; box-sizing: border-box; }
  html, body { width: 1200px; height: 1067px; overflow: hidden; background: var(--backdrop); }
  .canvas { position: relative; width: 1200px; height: 1067px; }
  .card {
    position: absolute; left: 294px; width: 612px; height: 377px;
    background: var(--card); overflow: hidden; color: var(--maroon);
  }
  .card--front { top: 138px; }
  .card--back { top: 551px; }

  .brand { position: absolute; font-family: "Saira", sans-serif; font-weight: 700; color: var(--maroon); line-height: 1; }
  .brand__name { display: block; }
  .brand__tag { display: block; }

  .front-lockup { position: absolute; left: 150px; top: 146px; display: flex; align-items: center; gap: 20px; }
  .front-lockup .mark-dot { width: 68px; height: 68px; border: 3px solid var(--maroon); border-radius: 50%; }
  .front-lockup .brand { position: static; }
  .front-lockup .brand__name { font-size: 29px; letter-spacing: 1px; }
  .front-lockup .brand__tag { font-size: 10px; letter-spacing: 5.2px; margin-top: 3px; }

  .back-brand { left: 39px; top: 50px; }
  .back-brand .brand__name { font-size: 35px; letter-spacing: 1.5px; }
  .back-brand .brand__tag { font-size: 13px; letter-spacing: 8.6px; margin-top: 6px; }

  .back-circle { position: absolute; left: 636px; top: 44px; width: 288px; height: 288px;
    border: 30px solid var(--maroon); border-radius: 50%; }

  .holder { position: absolute; left: 39px; top: 248px; font-family: "Saira", sans-serif; font-weight: 700; font-size: 24px; letter-spacing: 1px; text-transform: uppercase; }

  .contacts { position: absolute; left: 39px; top: 296px; list-style: none; font-family: "PT Sans", sans-serif; font-size: 14px; }
  .contacts li { display: flex; align-items: center; height: 20.5px; }
  .contacts svg { width: 12px; height: 12px; margin-right: 15px; fill: var(--maroon); }
</style>
</head>
<body>
<div class="canvas">
  <section class="card card--front">
    <div class="front-lockup">
      <div class="mark-dot"></div>
      <div class="brand">
        <span class="brand__name">BRINWOOD</span>
        <span class="brand__tag">AUTO HUB</span>
      </div>
    </div>
  </section>

  <section class="card card--back">
    <div class="brand back-brand">
      <span class="brand__name">BRINWOOD</span>
      <span class="brand__tag">AUTO HUB</span>
    </div>
    <div class="back-circle"></div>
    <p class="holder">Dean</p>
    <ul class="contacts">
      <li>
        <svg viewBox="0 0 12 12" aria-hidden="true"><path d="M1 3.5C1 2 2.5 1.5 6 1.5S11 2 11 3.5V5H8.5V4h-5v1H1z M3 6h6l1.5 4.5h-9z"/></svg>
        555-417-2386
      </li>
      <li>
        <svg viewBox="0 0 12 12" aria-hidden="true"><path d="M0.5 2.5h11v7h-11z M1.5 3.5 6 7l4.5-3.5" fill="none" stroke="#45201f" stroke-width="1.2"/></svg>
        Dean@BrinwoodAutoHub.example
      </li>
      <li>
        <svg viewBox="0 0 12 12" aria-hidden="true"><g fill="none" stroke="#45201f" stroke-width="1"><circle cx="6" cy="6" r="5"/><ellipse cx="6" cy="6" rx="2.2" ry="5"/><path d="M1 6h10"/></g></svg>
        www.BrinwoodAutoHub.example
      </li>
    </ul>
  </section>
</div>
</body>
</html>
```